Webdesign für die Veranstaltungsreihe Wolkenreigen
Zielgruppe
Für die Veranstaltungsreihe 'Wolkenreigen' soll ein Website-Design entwickelt werden, welches potentielle Besucher über die Veranstaltung informiert (Standorte, Anfahrt, Preise etc.) und gleichzeitig eine Foto- bzw. Videodokumentation der vergangenen 'Wolkenreigen' bietet.
Zielgruppe:
Personen jeder Altersgruppe, Gruppen wie (Familien, Vereine etc.)
Aufgabenstellung
Das Design sollte...
einfach und modern
nicht zu verspielt
freundlich
kreativ
innovativ
den Inhalt der Veranstaltungsreihe
...wiederspiegeln.
Bitte orientieren Sie sich an dem bestehenden Design der Eventreihe.

```html
<!DOCTYPE html>
<html lang="de">
<head>
<meta charset="utf-8">
<title>Wolkenreigen – Der Wettstreit der Pyrotechniker</title>
<link rel="stylesheet" href="https://fonts.googleapis.com/css2?family=Noto+Sans:wght@400;700&family=Fira+Sans+Condensed:wght@800&display=swap">
<style>
:root{
  --black:#000;
  --panel:#050505;
  --gold:#f5a623;
  --gold-light:#ffc54a;
  --gold-deep:#e8950f;
  --white:#fff;
  --glow-a:#8a5a18;
  --glow-b:#3a2106;
}
*{margin:0;padding:0;box-sizing:border-box}
html,body{width:960px;height:1200px;overflow:hidden;background:var(--black);color:var(--white);font-family:"Noto Sans",sans-serif}
.site{position:relative;width:960px;height:1200px}
.abs{position:absolute}

/* header */
.header{left:0;top:0;width:960px;height:302px;background:var(--black)}
.fireworks{left:280px;top:0;width:420px;height:240px;background:radial-gradient(ellipse at 50% 45%,#6b4410 0%,#3a1f08 40%,#180c04 62%,transparent 75%)}
.top-links{right:144px;top:24px;display:flex;align-items:center;gap:10px;font-size:10.5px;letter-spacing:.6px}
.sq{display:inline-block;width:17px;height:17px;border-radius:3px}
.sq.blue{background:#3b5998}
.sq.pink{background:#c13584}
.brand{left:0;top:92px;width:960px;text-align:center;font-family:"Fira Sans Condensed",sans-serif;font-weight:800;font-size:58px;line-height:1;color:var(--gold)}
.tagline{left:0;top:148px;width:960px;text-align:center;font-family:"Fira Sans Condensed",sans-serif;font-weight:800;font-size:19px;color:var(--white);letter-spacing:.3px}
.ticket-badge{left:854px;top:91px;width:91px;height:71px;border:2px solid var(--gold);border-radius:7px;display:flex;align-items:center;justify-content:center;text-align:center;font-weight:700;font-size:17px;line-height:1.15;color:var(--gold)}
.nav{left:0;top:262px;width:960px;height:24px}
.nav a{position:absolute;top:0;font-weight:700;font-size:14px;letter-spacing:1.3px;color:var(--gold);text-decoration:none}
.nav .sep{position:absolute;top:-7px;width:1px;height:36px;background:linear-gradient(transparent,#444,transparent)}

/* main */
.main-rule,.foot-rule{left:0;width:960px;height:3px;background:var(--gold-light)}
.main{left:0;top:305px;width:960px;height:763px;background:radial-gradient(ellipse at 20% 30%,var(--glow-a),var(--glow-b) 70%),var(--glow-b)}
.panel{left:120px;top:331px;width:720px;height:686px;background:var(--panel)}
.card{position:absolute;width:298px}
.card .rule{position:absolute;left:12px;top:0;width:274px;height:1px;background:linear-gradient(90deg,transparent,var(--gold-deep),transparent)}
.card h2{position:absolute;left:0;top:14px;width:298px;text-align:center;font-size:14px;font-weight:700;letter-spacing:1.2px;color:var(--gold)}
.card .photo{position:absolute;left:2px;top:42px;width:294px;height:166px}
.card .meta{position:absolute;left:2px;top:220px;width:294px;display:flex;justify-content:space-between;font-size:12.5px;letter-spacing:.6px}
.meta .ico{color:var(--gold);font-size:10px;margin-right:6px}
.card .btn{position:absolute;left:0;top:248px;width:298px;height:28px;border-radius:0 8px 8px 0;background:linear-gradient(var(--gold-light),var(--gold-deep));color:#111;font-size:10px;font-weight:700;letter-spacing:1px;display:flex;align-items:center;justify-content:center}

/* footer */
.footer{left:0;top:1071px;width:960px;height:129px;background:var(--black)}
.foot-row{position:absolute;left:0;width:960px;display:flex;justify-content:center;gap:18px;font-size:10.5px;letter-spacing:.6px}
.foot-icons{position:absolute;left:0;top:85px;width:960px;display:flex;justify-content:center;gap:23px}
</style>
</head>
<body>
<div class="site">
  <header class="abs header">
    <div class="abs fireworks" role="img" aria-label="Feuerwerk in Gold und Rosa über dem Schriftzug"></div>
    <div class="abs top-links"><span>Kontakt</span><span>|</span><span class="sq blue" style="margin-left:8px"></span><span class="sq pink" style="margin-left:6px"></span></div>
    <div class="abs brand">WOLKENREIGEN</div>
    <div class="abs tagline">DER WETTSTREIT DER PYROTECHNIKER</div>
    <div class="abs ticket-badge">Jetzt<br>Tickets<br>sichern!</div>
    <nav class="abs nav">
      <a style="left:157px">STARTSEITE</a><span class="sep" style="left:280px"></span>
      <a style="left:307px">STANDORTE</a><span class="sep" style="left:431px"></span>
      <a style="left:461px">DIE VERANSTALTUNG</a><span class="sep" style="left:651px"></span>
      <a style="left:675px">FOTOS &amp; VIDEOS</a>
    </nav>
  </header>

  <div class="abs main-rule" style="top:302px"></div>
  <main class="abs main" role="img" aria-label="Goldener Funkenregen als Hintergrund"></main>

  <section class="abs panel">
    <article class="card" style="left:45px;top:42px">
      <div class="rule"></div>
      <h2>WOLKENREIGEN BRAUNSCHWEIG</h2>
      <div class="photo" role="img" aria-label="Schloss in der Abenddämmerung" style="background:linear-gradient(#7ea9d8,#c9c2a2 55%,#4a4a4a)"></div>
      <div class="meta"><span><span class="ico">▦</span>18.Juni 2016</span><span><span class="ico">ⓘ</span>mehr Informationen</span></div>
      <div class="btn">JETZT TICKETS SICHERN!</div>
    </article>
    <article class="card" style="left:382px;top:42px">
      <div class="rule"></div>
      <h2>WOLKENREIGEN PADERBORN</h2>
      <div class="photo" role="img" aria-label="Beleuchtetes Schloss bei Nacht" style="background:linear-gradient(#1a1c26,#6a5210 40%,#d8a21a 65%,#1b1b1b)"></div>
      <div class="meta"><span><span class="ico">▦</span>13.August 2016</span><span><span class="ico">ⓘ</span>mehr Informationen</span></div>
      <div class="btn">JETZT TICKETS SICHERN!</div>
    </article>
    <article class="card" style="left:45px;top:365px">
      <div class="rule"></div>
      <h2>WOLKENREIGEN OBERHAUSEN</h2>
      <div class="photo" role="img" aria-label="Beleuchteter Gasometer mit Wasserbecken bei Nacht" style="background:linear-gradient(#2a1e14,#5a3a22 50%,#8a6a44 75%,#2c2418)"></div>
      <div class="meta"><span><span class="ico">▦</span>27.August 2016</span><span><span class="ico">ⓘ</span>mehr Informationen</span></div>
      <div class="btn">JETZT TICKETS SICHERN!</div>
    </article>
    <article class="card" style="left:382px;top:365px">
      <div class="rule"></div>
      <h2>WOLKENREIGEN KARLSRUHE</h2>
      <div class="photo" role="img" aria-label="Beleuchtetes Barockschloss bei Nacht" style="background:linear-gradient(#000 30%,#6e4414 50%,#b27a2a 60%,#111 72%)"></div>
      <div class="meta"><span><span class="ico">▦</span>Leider kein Termin 2016</span></div>
    </article>
  </section>

  <div class="abs foot-rule" style="top:1068px"></div>
  <footer class="abs footer">
    <div class="foot-row" style="top:32px"><span>Startseite</span><span>|</span><span>Standorte</span><span>|</span><span>Die Veranstaltung</span><span>|</span><span>Fotos&amp;Videos</span><span>|</span><span>Tickets sichern</span></div>
    <div class="foot-row" style="top:56px"><span>FAQ</span><span>|</span><span>AGB</span><span>|</span><span>Kontakt</span><span>|</span><span>Impressum</span></div>
    <div class="foot-icons"><span class="sq blue"></span><span class="sq pink"></span></div>
  </footer>
</div>
</body>
</html>
```